Amber Lark Prints

wall art that with words that inspire and can uplift people in their homes in times when they are down. An ever present presence to inspire that the subconscious takes in and subliminally feeds the home owner with positivity. Quotes... 1)In the morning, devour the prey, in the evening, divide the spoils. 2)Your situation is not your potential, but your potential depends on how you see your situation. 3)It is never too late, if your still here, then there is still time. 4)Busy your mind with the concepts of harmony, health, peace, and good will, and wonders will happen in your life. 5), it is hard to think straight while going around in circles. 6)you have everything you need to proceed. thses are just a few examples.
I would like to have colourful backgrounds. I am starting a online poster store and need a series of beautifully designed words and colours or pictures that go together like a song and it's two elements of words and music.

Target Market(s)

Anybody with a wall that wants an uplifting presence

Industry/Entity Type

Wall art, home decor

Font styles to use
Serif
Other font styles liked:
• stencil, Dead kansas, newspaper headline styles

Requirements
Must have
• I got to put that on my wall, it's amazing
Nice to have
• I am a martial artist, music producer, writer, lyricist that likes to inspire, and I also appreciate nature and beauty, how this can be incorporated into an artistic expression would be ideal elements. maybe also the colours of

```html
<!DOCTYPE html>
<html lang="en">
<head>
<meta charset="utf-8">
<title>Amber Lark Prints — Six Quotes</title>
<link rel="stylesheet" href="https://fonts.googleapis.com/css2?family=Montserrat:wght@400;900&display=swap">
<style>
  :root {
    --wall: #ebebea;
    --wall-shade: #dcdcda;
    --amber: #d4891f;
    --ink: #161616;
    --quote: #6e6e6e;
  }
  html, body {
    margin: 0;
    padding: 0;
    overflow: hidden;
    background: var(--wall);
  }
  .poster {
    display: block;
    width: 800px;
    height: 1200px;
  }
  .numeral {
    font-family: "Montserrat", sans-serif;
    font-weight: 900;
  }
  .amber { fill: var(--amber); }
  .ink { fill: var(--ink); }
  .quote {
    font-family: "Montserrat", sans-serif;
    font-weight: 400;
    font-size: 13px;
    fill: var(--quote);
    letter-spacing: 0.2px;
  }
</style>
</head>
<body>
<svg class="poster" viewBox="0 0 800 1200" xmlns="http://www.w3.org/2000/svg" aria-label="Six numbered inspirational quotes">
  <defs>
    <radialGradient id="wall-tone" cx="50%" cy="45%" r="75%">
      <stop offset="0%" stop-color="#f1f1f0"/>
      <stop offset="100%" stop-color="#dededc"/>
    </radialGradient>
    <clipPath id="five-top"><rect x="0" y="0" width="800" height="974"/></clipPath>
    <clipPath id="five-bottom"><rect x="0" y="974" width="800" height="300"/></clipPath>
    <clipPath id="six-band"><rect x="546" y="1061" width="216" height="112"/></clipPath>
  </defs>

  <rect class="wall" width="800" height="1200" fill="url(#wall-tone)"/>

  <!-- 1 -->
  <g class="figure-one">
    <rect class="amber" x="93" y="0" width="91" height="38"/>
    <rect class="amber" x="138" y="38" width="46" height="197"/>
    <rect class="ink" x="93" y="41" width="45" height="25"/>
    <rect class="ink" x="184" y="41" width="41" height="261"/>
  </g>

  <!-- 2 -->
  <g class="figure-two">
    <text class="numeral amber" x="496" y="419" font-size="378" text-anchor="middle">2</text>
    <rect class="ink" x="520" y="384" width="66" height="68"/>
    <rect class="amber" x="376" y="144" width="21" height="17"/>
    <rect class="amber" x="665" y="115" width="39" height="34"/>
  </g>

  <!-- 3 -->
  <g class="figure-three">
    <text class="numeral amber" x="154" y="714" font-size="375" text-anchor="middle">3</text>
    <rect class="ink" x="202" y="485" width="63" height="55"/>
  </g>

  <rect class="divider amber" x="347" y="509" width="12" height="223"/>

  <!-- 4 -->
  <g class="figure-four">
    <polygon class="amber" points="607,564 660,564 525,709 470,709"/>
    <rect class="amber" x="598" y="672" width="82" height="37"/>
    <rect class="ink" x="487" y="704" width="255" height="66"/>
    <rect class="ink" x="622" y="704" width="86" height="111"/>
    <rect class="ink" x="701" y="836" width="20" height="19"/>
  </g>

  <!-- 5 -->
  <g class="figure-five">
    <text class="numeral amber" x="322" y="1146" font-size="470" text-anchor="middle" clip-path="url(#five-bottom)">5</text>
    <text class="numeral ink" x="300" y="1146" font-size="470" text-anchor="middle" clip-path="url(#five-top)">5</text>
    <rect class="amber" x="196" y="983" width="21" height="19"/>
    <rect class="ink" x="48" y="1086" width="40" height="36"/>
  </g>

  <!-- 6 -->
  <g class="figure-six">
    <text class="numeral amber" x="735" y="1290" font-size="480" text-anchor="middle">6</text>
    <text class="numeral ink" x="700" y="1290" font-size="480" text-anchor="middle" clip-path="url(#six-band)">6</text>
  </g>

  <!-- quotes -->
  <text class="quote" transform="translate(241 255) rotate(-90)">
    <tspan x="0" y="10">In the morning, devour the</tspan>
    <tspan x="0" y="22.7">prey, in the evening, divide</tspan>
    <tspan x="0" y="35.4">the spoils.</tspan>
  </text>
  <text class="quote" transform="translate(618 451) rotate(-90)">
    <tspan x="0" y="10">Your situation is not your potential,</tspan>
    <tspan x="0" y="22.7">but your potential depends on</tspan>
    <tspan x="0" y="35.4">how you see your situation.</tspan>
  </text>
  <text class="quote" transform="translate(286 704) rotate(-90)">
    <tspan x="0" y="10">It is never too late, if your still</tspan>
    <tspan x="0" y="22.7">here, then there is still time.</tspan>
  </text>
  <text class="quote" transform="translate(395 785) rotate(-90)">
    <tspan x="0" y="10">Busy your mind with the</tspan>
    <tspan x="0" y="22.7">concepts of harmony,</tspan>
    <tspan x="0" y="35.4">health, peace, and good will,</tspan>
    <tspan x="0" y="48.1">and wonders will happen in</tspan>
    <tspan x="0" y="60.8">your life.</tspan>
  </text>
  <text class="quote" transform="translate(118 1086) rotate(-90)">
    <tspan x="0" y="10">It is hard to think straight</tspan>
    <tspan x="0" y="22.7">while going around in circles.</tspan>
  </text>
  <text class="quote" transform="translate(501 1135) rotate(-90)">
    <tspan x="0" y="10">You have everything</tspan>
    <tspan x="0" y="22.7">you need to proceed.</tspan>
  </text>
</svg>
</body>
</html>
```